Business Card Design Project for - The Pellowick Greenworks Company Ltd. We are a Landscape and garden

I would like designer to use all special glosses etc so i can have a professional looking business card. The theme of the business card can reflect that of the Logo attached by MarkQuarry or your own unique ideas.. please feel free to go wild as i hope i can select a winner i like - my budget will be committed so please get involved. Good luck and thank you Lyndon

Target Market(s)

Must look Professional

General Public and Businesses including Councils, Local Government, Hospitals, Hotels, Professionals and Professional Sports People.

Industry/Entity Type

Landscape Gardening

Contact Information for Business Card

The Pellowick Greenworks Company Ltd

Mr L.R Ashcombe
Head Office - Quayfront Park Manchester
t. 0772 408 916
e. info@pellowickgreenworks.co.uk
w. www.pellowickgreenworks.co.uk

Facebook - https://www.friendpage-example.com/ThePellowickGreenworksCompany/
Twitter - https://chirpline-example.com/ThePruningCart
Instagram - https://www.snapgrid-example.com/thepellowickgreenworkscompany/?hl=en
Google+ - https://circles.searchhub-example.com/u/0/208473950162438571093
Yelp - https://www.reviewnook-example.co.uk/biz/the-pellowick-greenworks-company-manchester-4

Font styles to use
Serif
Script
Other font styles liked:
• I don't have much of an idea of font types sorry

Colors

Designer to choose colors to be used in the design.

Requirements
Must have
• A Professional look and Design
• Special effects with gloss and fading of colours possibly..
• Front and back design
Nice to have
• All special features with effects and gloss etc

```html
<!DOCTYPE html>
<html lang="en">
<head>
<meta charset="utf-8">
<title>The Pellowick Greenworks Company Ltd – Business Card</title>
<link rel="stylesheet" href="https://fonts.googleapis.com/css2?family=Cinzel:wght@400;600&family=Roboto+Condensed:wght@400;700&display=swap">
<style>
  :root {
    --stage: #4a4a4c;
    --card-black: #0d0d0e;
    --card-black-edge: #232325;
    --card-white: #ffffff;
    --green-deep: #2f9e2a;
    --green-mid: #5cbf2f;
    --green-light: #c9ea3c;
    --brand-grey: #8a8a8a;
    --brand-silver: #cfcfcf;
    --ink: #1c1c1c;
    --ink-soft: #333333;
    --dot-1: #d93a3a;
    --dot-2: #2fa3e0;
    --dot-3: #c8457a;
    --dot-4: #d9493c;
    --dot-5: #3b5a9a;
  }
  * { box-sizing: border-box; margin: 0; padding: 0; }
  html, body { width: 1200px; height: 852px; overflow: hidden; }
  body {
    background: var(--stage);
    position: relative;
    font-family: "Roboto Condensed", Arial, sans-serif;
  }
  .card {
    position: absolute;
    top: 256px;
    width: 530px;
    height: 340px;
    border-radius: 22px;
    overflow: hidden;
    box-shadow: 0 14px 30px rgba(0,0,0,.45);
  }
  /* Card back */
  .card-back {
    left: 45px;
    background: radial-gradient(ellipse at 55% 35%, var(--card-black-edge), var(--card-black) 70%);
  }
  .card-back .gloss {
    position: absolute; inset: 0;
    background: linear-gradient(115deg, transparent 35%, rgba(255,255,255,.07) 48%, transparent 60%);
  }
  .brand {
    position: absolute;
    display: flex;
    align-items: center;
    gap: 14px;
    font-family: "Cinzel", Georgia, serif;
    font-weight: 400;
    white-space: nowrap;
  }
  .brand-dot {
    width: 46px; height: 46px;
    border-radius: 50%;
    background: linear-gradient(135deg, var(--green-light), var(--green-deep));
    flex: none;
  }
  .brand-name { line-height: 1.05; }
  .brand-name .main { display: block; font-size: 34px; letter-spacing: 1px; }
  .brand-name .sub  { display: block; font-size: 14px; letter-spacing: 3px; margin-top: 4px; }
  .card-back .brand { left: 50%; top: 50%; transform: translate(-50%, -50%); color: var(--brand-silver); }

  /* Card front */
  .card-front { left: 625px; background: var(--card-white); }
  .card-front .swoosh { position: absolute; inset: 0; }
  .holder {
    position: absolute; right: 30px; top: 18px;
    text-align: right; color: var(--ink);
  }
  .holder .name {
    font-family: "Cinzel", Georgia, serif;
    font-weight: 600; font-size: 22px; letter-spacing: 1px;
  }
  .holder .office { font-size: 12px; margin-top: 2px; }
  .card-front .brand { left: 26px; top: 186px; color: var(--brand-grey); }
  .card-front .brand-dot { width: 40px; height: 40px; }
  .card-front .brand-name .main { font-size: 26px; }
  .card-front .brand-name .sub { font-size: 11px; letter-spacing: 2.4px; }

  .contact {
    position: absolute; left: 26px; bottom: 20px;
    list-style: none; font-size: 13px; font-weight: 700; color: var(--ink);
  }
  .contact li { display: flex; align-items: center; gap: 8px; height: 17px; }
  .contact svg { width: 12px; height: 12px; fill: var(--green-deep); flex: none; }

  .social {
    position: absolute; right: 24px; top: 240px;
    list-style: none; font-size: 12px; color: var(--ink-soft); text-align: right;
  }
  .social li { display: flex; justify-content: flex-end; align-items: center; gap: 8px; height: 17px; }
  .social .dot { width: 11px; height: 11px; border-radius: 50%; flex: none; }
  .social li:nth-child(1) .dot { background: var(--dot-1); }
  .social li:nth-child(2) .dot { background: var(--dot-2); }
  .social li:nth-child(3) .dot { background: var(--dot-3); }
  .social li:nth-child(4) .dot { background: var(--dot-4); }
  .social li:nth-child(5) .dot { background: var(--dot-5); }
</style>
</head>
<body>

<section class="card card-back" aria-label="Card back">
  <div class="gloss"></div>
  <div class="brand">
    <span class="brand-dot"></span>
    <span class="brand-name">
      <span class="main">THE PELLOWICK</span>
      <span class="sub">GREENWORKS COMPANY LTD</span>
    </span>
  </div>
</section>

<section class="card card-front" aria-label="Card front">
  <svg class="swoosh" viewBox="0 0 530 340" preserveAspectRatio="none" aria-hidden="true">
    <defs>
      <linearGradient id="band" x1="0" y1="1" x2="1" y2="0">
        <stop offset="0" stop-color="var(--green-deep)"/>
        <stop offset=".5" stop-color="var(--green-mid)"/>
        <stop offset="1" stop-color="var(--green-light)"/>
      </linearGradient>
    </defs>
    <path d="M0 0 H530 V80 C420 100 330 96 230 102 C130 108 60 122 0 140 Z" fill="url(#band)"/>
    <path d="M0 154 C80 132 160 118 260 112 C360 106 450 106 530 90 V100 C450 118 360 120 260 126 C170 132 80 148 0 168 Z" fill="url(#band)"/>
    <path d="M0 178 C90 156 170 140 270 134 C360 128 450 126 530 108" fill="none" stroke="var(--green-mid)" stroke-width="2"/>
  </svg>

  <div class="holder">
    <p class="name">MR L.R ASHCOMBE</p>
    <p class="office">Head Office - Quayfront Park Manchester</p>
  </div>

  <div class="brand">
    <span class="brand-dot"></span>
    <span class="brand-name">
      <span class="main">THE PELLOWICK</span>
      <span class="sub">GREENWORKS COMPANY LTD</span>
    </span>
  </div>

  <ul class="social">
    <li>ThePruningCart<span class="dot"></span></li>
    <li>thepellowickgreenworkscompany<span class="dot"></span></li>
    <li>208473950162438571093<span class="dot"></span></li>
    <li>ThePellowickGreenworksCompany<span class="dot"></span></li>
    <li>the-pellowick-greenworks-company-manchester<span class="dot"></span></li>
  </ul>

  <ul class="contact">
    <li><svg viewBox="0 0 24 24"><path d="M6.6 10.8a15 15 0 0 0 6.6 6.6l2.2-2.2a1 1 0 0 1 1-.25 11.4 11.4 0 0 0 3.6.57 1 1 0 0 1 1 1V20a1 1 0 0 1-1 1A17 17 0 0 1 3 4a1 1 0 0 1 1-1h3.5a1 1 0 0 1 1 1c0 1.25.2 2.45.57 3.57a1 1 0 0 1-.25 1z"/></svg>0772 408 916</li>
    <li><svg viewBox="0 0 24 24"><path d="M2 5h20v14H2z M2 5l10 8 10-8" /></svg>info@pellowickgreenworks.co.uk</li>
    <li><svg viewBox="0 0 24 24"><circle cx="12" cy="12" r="10"/></svg>www.pellowickgreenworks.co.uk</li>
  </ul>
</section>

</body>
</html>
```